Funky physio needs a business card to match!

We are a physiotherapy clinic and pilates studio who specialise in sports and spinal injuries, as well as persistent or chronic pain.

We would like a vibrant and fun business card which is not over medicalised.
Updates

PO Box number is 418

Industry/Entity Type

Clinic

Contact Information for Business Card

Tidewell Sports Medicine
Suite 4 & 5 Marlowe St, KELBROOK VIC 3188
p 86203917
f 9481 3057
e admin@tidewellsportsmedicine.com.au
w tidewellsportsmedicine.com.au

All correspondence via email or mailed to:
PO Box
KELBROOK VIC 3188

Requirements
Must have
• Must have a green element - see logo. I don't mind if the business card is green, or if it's black, grey, white etc with green highlights. I'm the physio ... you're the designer!!!! It just needs to "look" green!
Our font is Harabara and can be downloaded from glyphbarn.com
Nice to have
• Please check our website to get a feel of our company. We don't take ourselves to seriously, however want to be taken seriously!
Should not have
• not over medicalised or corporate

```html
<!DOCTYPE html>
<html lang="en">
<head>
<meta charset="utf-8">
<title>Tidewell Sports Medicine – Business Card</title>
<link rel="stylesheet" href="https://fonts.googleapis.com/css2?family=Arimo:wght@400;700&display=swap">
<style>
  :root {
    --green: #76ad3d;
    --green-dark: #4f8a23;
    --ink: #2a2a2a;
    --paper: #ffffff;
    --backdrop: #ececec;
  }
  * { box-sizing: border-box; margin: 0; padding: 0; }
  html, body { width: 1200px; height: 901px; overflow: hidden; }
  body {
    background: var(--backdrop);
    font-family: "Arimo", Arial, sans-serif;
    position: relative;
  }
  .card {
    position: absolute;
    top: 300px;
    width: 520px;
    height: 300px;
    background: var(--paper);
    box-shadow: 0 4px 14px rgba(0,0,0,0.12);
    overflow: hidden;
  }
  .card--front { left: 50px; }
  .card--back { left: 630px; }

  .band {
    position: absolute;
    left: 0; right: 0;
    background: var(--green);
  }
  .mark {
    position: absolute;
    border-radius: 50%;
    background: var(--paper);
    border: 6px solid var(--green-dark);
  }
  .brand-name {
    position: absolute;
    color: var(--paper);
    font-weight: 700;
    white-space: nowrap;
  }

  /* Front */
  .card--front .band { top: 100px; height: 72px; }
  .card--front .mark { left: 40px; top: 80px; width: 112px; height: 112px; }
  .card--front .brand-name { left: 168px; top: 122px; font-size: 26px; }
  .card--front .web {
    position: absolute;
    right: 30px; top: 184px;
    color: var(--green-dark);
    font-size: 18px;
  }

  /* Back */
  .card--back .band--top { top: 42px; height: 56px; }
  .card--back .band--bottom { top: 250px; height: 28px; }
  .card--back .mark { left: 30px; top: 24px; width: 92px; height: 92px; }
  .card--back .brand-name { left: 138px; top: 57px; font-size: 23px; }
  .address {
    position: absolute;
    left: 200px; top: 114px;
    width: 270px;
    text-align: center;
    font-size: 12.5px;
    line-height: 1.35;
    color: var(--ink);
    font-style: normal;
  }
  .online {
    position: absolute;
    left: 22px; top: 188px;
    font-size: 11.5px;
    line-height: 1.4;
    color: var(--ink);
  }
  .label { color: var(--green); }
  .phones {
    position: absolute;
    right: 24px; top: 212px;
    font-size: 12px;
    line-height: 1.35;
    color: var(--ink);
  }
</style>
</head>
<body>
  <section class="card card--front" aria-label="Business card front">
    <div class="band"></div>
    <div class="mark" aria-hidden="true"></div>
    <div class="brand-name">Tidewell Sports Medicine</div>
    <div class="web">www.tidewellsportsmedicine.com.au</div>
  </section>

  <section class="card card--back" aria-label="Business card back">
    <div class="band band--top"></div>
    <div class="mark" aria-hidden="true"></div>
    <div class="brand-name">Tidewell Sports Medicine</div>
    <address class="address">
      Suite 4 &amp; 5 Marlowe St.<br>
      KELBROOK VIC 3188<br>
      All correspondence via email or mailed<br>
      To: PO Box 418 KELBROOK VIC 3188
    </address>
    <div class="online">
      <span class="label">e-mail:</span> admin@tidewellsportsmedicine.com.au<br>
      <span class="label">www:</span> tidewellsportsmedicine.com.au
    </div>
    <div class="phones">
      <span class="label">phone:</span> 86203917<br>
      <span class="label">fax:</span> 9481 3057
    </div>
    <div class="band band--bottom"></div>
  </section>
</body>
</html>
```